Harlow Mead Brewery website design,

I would like a website designed for my microbrewery, with a part that you can purchase beers from, links to our social media. The brand is luxury, old English, classic, timeless, simple, crisp and clean. I’d like to send you a design we have for the beer can so you can get understanding of what we are trying to achieve.

Please have a look at our Instagram and Facebook to get an understanding of what we are about.

Thank you.

Neil

Target Market(s)

Non beardy beer drinkers. Young, professional, seeking experiences and something to remember.

Industry/Entity Type

Brewery

Font styles to use
Other font styles liked:
• I will upload photos of what I’d like.

Colors

Designer to choose colors to be used in the design.

Requirements
Must have
• Photos of our beers, it must be a beautiful website, landing page video background of a beer slowly being poured into a glass.
Nice to have
• Shots of hops, grain, videos of steam from the brewing process.

```html
<!DOCTYPE html>
<html lang="en">
<head>
<meta charset="utf-8">
<title>Harlow Mead Brewery</title>
<link rel="stylesheet" href="https://fonts.googleapis.com/css2?family=Open+Sans:wght@400;600;700&family=Oswald:wght@400;500&family=Dancing+Script:wght@600;700&family=Great+Vibes&display=swap">
<style>
:root{
  --black:#000;
  --panel:#0c0c0c;
  --card:#1b1b1b;
  --gold:#c39b55;
  --gold-soft:#b8985e;
  --white:#fff;
  --muted:#cfcfcf;
  --line:#3a3a3a;
}
*{box-sizing:border-box;margin:0;padding:0}
html,body{width:1200px;height:3495px;overflow:hidden;background:var(--black);color:var(--white);font-family:"Open Sans",Arial,sans-serif}
.page{position:relative;width:1200px;height:3495px}
.abs{position:absolute}

/* header */
.site-header{position:absolute;left:0;top:0;width:1200px;height:93px;background:#111;border-bottom:1px solid #2b2b2b;z-index:3}
.tagline{left:100px;top:10px;font-size:13px;color:var(--white);display:flex;align-items:center;gap:8px}
.tagline .dot{width:10px;height:10px;border:2px solid var(--gold);border-radius:50%}
.follow{right:100px;top:10px;font-size:13px;display:flex;gap:14px;align-items:center}
.follow i{display:block;width:12px;height:12px;border-radius:50%;background:var(--white)}
.nav{top:52px;font-size:12px;font-weight:600;letter-spacing:.5px;display:flex}
.nav a{color:var(--white);text-decoration:none}
.nav.left{left:222px}
.nav.left a{margin-right:72px}
.nav.right{left:755px}
.nav.right a{margin-right:76px}
.logo-cap{left:515px;top:0;width:170px;height:130px;background:#111;border-radius:0 0 85px 85px;border-bottom:2px solid var(--gold);display:flex;align-items:center;justify-content:center;z-index:4}
.brand-name{font-family:"Open Sans",Arial,sans-serif;font-weight:700;color:var(--gold);font-size:44px;letter-spacing:2px}
.tools{right:100px;top:50px;display:flex;gap:34px;z-index:5}

/* hero */
.hero{left:0;top:93px;width:1200px;height:527px;background:linear-gradient(90deg,#1a1a1a 0%,#3b3b3b 40%,#6a6a6a 62%,#2a2a2a 100%)}
.hero-can{left:55px;top:70px;width:175px;height:315px;border-radius:18px;background:linear-gradient(90deg,#0a0a0a,#2a2a2a 50%,#0a0a0a);border-top:34px solid #c9a84f}
.hero-text{left:0;width:1200px;top:160px;text-align:center}
.hero-quote{font-family:"Oswald",Arial,sans-serif;font-size:25px;line-height:29px;text-transform:uppercase;color:var(--white);text-shadow:0 1px 3px #000}
.hero-sign{font-family:"Dancing Script",cursive;font-size:34px;color:var(--gold);margin-top:6px;line-height:40px}
.hero-sub{font-family:"Dancing Script",cursive;font-size:24px;color:var(--white);margin-top:6px}
.dots{left:574px;top:446px;display:flex;gap:12px}
.dots i{width:8px;height:8px;border-radius:50%;background:var(--white)}
.dots i:first-child{background:var(--gold)}
.arrow{top:345px}
.rule{left:0;top:620px;width:1200px;height:2px;background:#8a8a8a}

/* welcome */
.welcome{left:0;top:622px;width:1200px;height:405px;background:linear-gradient(90deg,#111 0%,#1a1a1a 50%,#0d0d0d 100%)}
.script{font-family:"Dancing Script",cursive;color:var(--gold)}
.welcome .script{left:100px;top:50px;font-size:44px}
.welcome h2{left:100px;top:112px;font-weight:400;font-size:25px;letter-spacing:.5px}
.body-text{font-size:12.5px;line-height:20px;color:var(--muted)}
.welcome .p1{left:100px;top:155px;width:500px}
.welcome h3{left:100px;top:218px;font-weight:400;font-size:25px}
.welcome .p2{left:100px;top:258px;width:500px}
.welcome .p2 em{color:#8fb0d8;font-style:normal}
.beer-hand{left:688px;top:12px;width:246px;height:290px;background:linear-gradient(90deg,#e8b83a 0%,#f5d779 35%,#d9a074 75%,#c27f5a 100%);border-radius:10px 40px 40px 10px}

/* menu */
.menu{left:0;top:1027px;width:1200px;height:500px}
.menu-tabs{left:100px;top:120px;width:231px}
.menu-tabs li{list-style:none;height:62px;line-height:62px;padding-left:16px;font-size:18px;color:var(--gold)}
.menu-tabs li.active{background:#252525;color:var(--white)}
.menu-divider{left:331px;top:0;width:2px;height:500px;background:#555}
.menu-body{left:356px;top:55px;width:420px}
.menu-body h3{font-weight:400;font-size:25px;letter-spacing:.5px}
.menu-body .intro{font-size:11.5px;color:var(--muted);margin-top:6px}
.menu-item{position:relative;margin-top:22px;height:95px}
.menu-item .name{font-size:15px;color:var(--gold);width:225px;line-height:22px}
.menu-item .desc{font-size:11.5px;line-height:21px;color:var(--muted);width:240px;margin-top:6px}
.menu-item .price{position:absolute;left:299px;top:36px;font-size:20px;color:var(--white)}

/* news */
.news-title{left:100px;top:1597px;font-size:42px;letter-spacing:2px}
.news-card{top:1687px;width:316px;height:425px;background:var(--card)}
.news-card .photo{height:213px;background:linear-gradient(180deg,#4a3a2a,#8b6a42 55%,#2a2018)}
.news-card .photo.stout{background:radial-gradient(ellipse at 50% 45%,#2a170c 30%,#c9a27a 40%,#3a3a3a 60%,#151515 100%)}
.news-card .text{padding:24px 22px 0;text-align:center;font-size:12.5px;line-height:21px;color:var(--muted);height:150px}
.news-card h4{font-weight:600;font-size:20px;color:var(--white);margin-bottom:10px}
.news-card .stats{position:absolute;left:0;bottom:0;width:100%;height:62px;background:var(--gold-soft);display:flex;justify-content:center;gap:30px;align-items:center;font-size:11.5px;color:#2a2a2a}
.news-card .stats span{display:flex;align-items:center;gap:6px}

/* contact */
.contact{left:0;top:2144px;width:1200px;height:477px}
.mug{left:0;top:150px;width:256px;height:327px;background:linear-gradient(180deg,#f4efe2 0%,#f4efe2 22%,#f2b632 30%,#e89a1b 70%,#c77510 100%);border-radius:0 30px 0 0}
.server{left:908px;top:0;width:292px;height:477px;background:linear-gradient(180deg,#1a0f08 0%,#b87a4a 30%,#e8b04a 60%,#b01e1e 85%,#101010 100%);border-radius:140px 0 0 0}
.contact h2{left:0;width:1200px;top:105px;text-align:center;font-family:"Great Vibes",cursive;font-weight:400;font-size:92px;line-height:110px;word-spacing:14px}
.contact .info{left:298px;top:238px;width:200px;text-align:right;font-size:14px;line-height:20px}
.circle{width:70px;height:70px;border:2px solid var(--white);border-radius:50%;display:flex;align-items:center;justify-content:center}
.contact .c1{left:518px;top:228px}
.contact .c2{left:610px;top:228px}
.contact .addr{left:610px;top:305px;font-size:14px;line-height:20px}
.strip{left:0;top:2621px;width:1200px;height:159px;display:flex}
.strip div{flex:1}

/* updates */
.updates .script{left:100px;top:2840px;font-size:26px}
.updates h2{left:100px;top:2868px;font-weight:400;font-size:32px}
.subscribe{left:613px;top:2867px;width:487px;height:46px;display:flex}
.subscribe .field{flex:1;border:1px solid #6a6a6a;background:#000}
.subscribe .btn{width:114px;background:var(--gold-soft);color:#222;font-size:13px;display:flex;align-items:center;justify-content:center;letter-spacing:.5px}

/* footer */
.site-footer{left:0;top:2960px;width:1200px;height:535px;background:linear-gradient(180deg,#000 0%,#000 50%,#1c140d 80%,#2a1d12 100%)}
.footer-logo{left:490px;top:0;width:220px;height:210px;border-bottom:2px solid var(--gold);border-radius:0 0 110px 110px;display:flex;align-items:center;justify-content:center}
.footer-col{top:280px;width:360px;text-align:center}
.footer-col h5{font-weight:400;font-size:21px;color:var(--white)}
.footer-col p{font-size:19px;line-height:27px;color:var(--gold);margin-top:2px}
.socials{left:505px;top:423px;display:flex;gap:55px}
.socials i{display:block;width:44px;height:44px;background:var(--gold-soft)}
</style>
</head>
<body>
<div class="page">

  <header class="site-header">
    <div class="abs tagline"><span class="dot"></span>Approved &amp; Originality</div>
    <div class="abs follow">Follow us <i aria-label="Social link"></i><i aria-label="Social link"></i><i aria-label="Social link"></i></div>
    <nav class="abs nav left"><a>HOME</a><a>ABOUT</a><a>OUR BEERS</a></nav>
    <nav class="abs nav right"><a>SHOP</a><a>BLOG</a><a>CONTACT</a></nav>
    <div class="abs tools">
      <svg width="14" height="14" viewBox="0 0 14 14"><circle cx="6" cy="6" r="4.5" fill="none" stroke="#c39b55" stroke-width="2"/><line x1="9.5" y1="9.5" x2="13" y2="13" stroke="#c39b55" stroke-width="2"/></svg>
      <svg width="14" height="14" viewBox="0 0 14 14"><rect y="2" width="14" height="2" fill="#c39b55"/><rect y="6" width="14" height="2" fill="#c39b55"/><rect y="10" width="14" height="2" fill="#c39b55"/></svg>
    </div>
  </header>
  <div class="abs logo-cap"><span class="brand-name">HMB</span></div>

  <section class="abs hero">
    <div class="abs hero-can" role="img" aria-label="Black porter can with gold lid"></div>
    <div class="abs hero-text">
      <p class="hero-quote">Some say, the ingredients for this porter are extracted from<br>hens teeth found only in the lair of a mystical unicorn</p>
      <p class="hero-sign">Harlow Mead Brewery</p>
      <p class="hero-sub">Some Friends Saya</p>
    </div>
    <svg class="abs arrow" style="left:12px" width="10" height="16" viewBox="0 0 10 16"><path d="M8 2 2 8l6 6" fill="none" stroke="#fff" stroke-width="2"/></svg>
    <svg class="abs arrow" style="right:12px" width="10" height="16" viewBox="0 0 10 16"><path d="m2 2 6 6-6 6" fill="none" stroke="#fff" stroke-width="2"/></svg>
    <div class="abs dots"><i></i><i></i><i></i></div>
  </section>
  <div class="abs rule"></div>

  <section class="abs welcome" aria-label="Welcome">
    <p class="abs script">Welcome!</p>
    <h2 class="abs">MAKING THE BEST BEER POSSIBLE</h2>
    <p class="abs body-text p1">We are a Micro-brewery in the basement of Harlow Mead, Martin and Neil brew most Mondays or Tuesdays... Harlow Porter, Captain Hal and Last Orders, 3 exceptional beers...</p>
    <h3 class="abs">HMB'S BEER</h3>
    <p class="abs body-text p2">All of our beers are brewed with malted barley from <em>Ashcombe Maltings. This is the</em> closest maltings to us but more importantly preserves the old way of doing things. Producing malted barley from locally grown crops where possible, they still rake, plough and turn the malt on raised floors by hand.</p>
    <div class="abs beer-hand" role="img" aria-label="Hand holding a frothy mug of golden beer"></div>
  </section>

  <section class="abs menu">
    <ul class="abs menu-tabs">
      <li class="active">IBERIAN SHOOTER</li>
      <li>HARLOW PORTER</li>
      <li>CAPTAIN HAL</li>
      <li>THE BARON</li>
    </ul>
    <div class="abs menu-divider"></div>
    <div class="abs menu-body">
      <h3>IBERIAN SHOOTER</h3>
      <p class="intro">nisi elit consequat ipsum, nec sagittis sem nibh id elit.</p>
      <div class="menu-item"><p class="name">IBERIAN SHOOTER --------- 100 ml</p><p class="desc">Includes dry vermouth and olive brine shaken with ice and served with an olive</p><span class="price">$ 15.00</span></div>
      <div class="menu-item"><p class="name">IBERIAN SHOOTER --------- 200 ml</p><p class="desc">Includes dry vermouth and olive brine shaken with ice and served with an olive</p><span class="price">$ 35.00</span></div>
      <div class="menu-item"><p class="name">IBERIAN SHOOTER --------- 350 ml</p><p class="desc">Includes dry vermouth and olive brine shaken with ice and served with an olive</p><span class="price">$ 65.00</span></div>
    </div>
  </section>

  <h2 class="abs script news-title">Latest News !</h2>

  <article class="abs news-card" style="left:100px">
    <div class="photo" role="img" aria-label="Brewery cellar with ladder"></div>
    <div class="text">Our tiny little brewrig will become the brewlab soon, making way for the beast. Exciting times, made another porter last night, now experimenting with kegging methods.... all in good time. Happy Wednesday everyone.</div>
    <div class="stats"><span>16 &#9829;</span><span>0 &#9679;</span><span>03 &#10148;</span></div>
  </article>
  <article class="abs news-card" style="left:442px">
    <div class="photo" role="img" aria-label="Brewery cellar with ladder"></div>
    <div class="text">Our tiny little brewrig will become the brewlab soon, making way for the beast. Exciting times, made another porter last night, now experimenting with kegging methods.... all in good time. Happy Wednesday everyone.</div>
    <div class="stats"><span>16 &#9829;</span><span>0 &#9679;</span><span>03 &#10148;</span></div>
  </article>
  <article class="abs news-card" style="left:784px;height:400px">
    <div class="photo stout" role="img" aria-label="Glass of dark porter with creamy head"></div>
    <div class="text" style="height:125px"><h4>EVERY SATURDAY NIGHTS</h4>We are often asked how we brewed such a great Porter, what's the secret.... don't tell anyone, but here is it, are you ready?</div>
    <div class="stats"><span>16 &#9829;</span><span>0 &#9679;</span><span>03 &#10148;</span></div>
  </article>

  <section class="abs contact">
    <div class="abs mug" role="img" aria-label="Glass mug of golden beer with foam"></div>
    <div class="abs server" role="img" aria-label="Waitress in traditional dress carrying beer mugs"></div>
    <h2 class="abs">Contact Us</h2>
    <p class="abs info">Our Contact Information<br>+44 7700 900123</p>
    <div class="abs circle c1"><svg width="26" height="26" viewBox="0 0 24 24"><path d="M6.6 10.8a15 15 0 0 0 6.6 6.6l2.2-2.2c.3-.3.7-.4 1-.2 1.1.4 2.3.6 3.6.6.6 0 1 .4 1 1V20c0 .6-.4 1-1 1A17 17 0 0 1 3 4c0-.6.4-1 1-1h3.5c.6 0 1 .4 1 1 0 1.3.2 2.5.6 3.6.1.3 0 .7-.2 1z" fill="#fff"/></svg></div>
    <div class="abs circle c2"><svg width="26" height="26" viewBox="0 0 24 24"><path d="M5 2v20" stroke="#fff" stroke-width="2"/><path d="M6 3h13l-3 5 3 5H6z" fill="#fff"/></svg></div>
    <p class="abs addr">Thornbury Vale,<br>Wessex, United Kingdom</p>
  </section>
  <div class="abs strip" role="img" aria-label="Row of bar photos: drinks, whisky glasses, bartender, barrels">
    <div style="background:linear-gradient(135deg,#2a1a14,#8a5a44)"></div>
    <div style="background:linear-gradient(135deg,#3a1e0a,#c07a2a)"></div>
    <div style="background:linear-gradient(135deg,#1a1410,#6a4a2a)"></div>
    <div style="background:linear-gradient(135deg,#302822,#a08060)"></div>
    <div style="background:linear-gradient(135deg,#4a2a12,#9a6a3a)"></div>
  </div>

  <section class="updates">
    <p class="abs script">Get Updates</p>
    <h2 class="abs">Stay In Touch With Updates</h2>
    <div class="abs subscribe"><div class="field"></div><div class="btn">SUBSCRIBE</div></div>
  </section>

  <footer class="abs site-footer">
    <div class="abs footer-logo"><span class="brand-name" style="font-size:54px">HMB</span></div>
    <div class="abs footer-col" style="left:80px"><h5>Call us</h5><p>+44 7700 900123</p></div>
    <div class="abs footer-col" style="left:420px"><h5>Address</h5><p>Thornbury Vale, Wessex, United<br>Kingdom</p></div>
    <div class="abs footer-col" style="left:760px"><h5>Email</h5><p>support@harlowmead.com</p></div>
    <div class="abs socials"><i aria-label="Social link"></i><i aria-label="Social link"></i><i aria-label="Social link"></i></div>
  </footer>

</div>
</body>
</html>
```